Business cards for law firm with global theme

I'd like business cards with contact info for two offices. They should include the colors and font of the new logo design, which is a stylized globe with an "F" in it. The feel should be very modern and professional.

```html
<!DOCTYPE html>
<html lang="en">
<head>
<meta charset="utf-8">
<title>Marwell Law – Business Cards</title>
<link rel="stylesheet" href="https://fonts.googleapis.com/css2?family=Arimo:wght@400;700&display=swap">
<style>
  :root {
    --navy: #0c3a6c;
    --navy-deep: #062c57;
    --navy-light: #0b5488;
    --sky: #1b98d5;
    --paper: #f7f8f9;
    --ink: #3d3d3d;
    --muted: #5a5a5a;
    --backdrop: #e6e8eb;
  }
  * { box-sizing: border-box; margin: 0; padding: 0; }
  html, body {
    width: 1200px; height: 768px; overflow: hidden;
    background: var(--backdrop);
    font-family: "Arimo", Arial, sans-serif;
  }
  .sheet {
    position: relative; width: 1200px; height: 768px;
    display: flex; align-items: center; justify-content: center; gap: 60px;
  }
  .card {
    position: relative; width: 520px; height: 300px;
    border-radius: 18px; overflow: hidden;
    box-shadow: 0 8px 24px rgba(0,0,0,0.18);
  }

  /* Back side */
  .card--back {
    background: linear-gradient(120deg, var(--navy-deep) 0%, var(--navy) 55%, var(--navy-light) 100%);
    display: flex; flex-direction: column; align-items: center; justify-content: center; gap: 18px;
  }
  .brand { display: flex; align-items: center; gap: 14px; }
  .brand__dot { width: 62px; height: 62px; border-radius: 50%; background: var(--sky); flex: none; }
  .brand__name {
    font-weight: 700; font-size: 40px; letter-spacing: 1px; text-transform: uppercase;
  }
  .card--back .brand { flex-direction: column; gap: 16px; }
  .card--back .brand__dot { width: 80px; height: 80px; }
  .card--back .brand__name { color: #ffffff; font-size: 44px; }
  .rule { height: 2px; background: var(--sky); width: 300px; }

  /* Front side */
  .card--front { background: var(--paper); }
  .card--front .brand { position: absolute; top: 44px; left: 120px; }
  .card--front .brand__name { color: var(--navy); font-size: 36px; }
  .card--front .rule { position: absolute; top: 118px; left: 200px; width: 270px; }

  .person {
    position: absolute; top: 150px; left: 40px; width: 200px; text-align: right;
  }
  .person__name { color: var(--navy); font-weight: 700; font-size: 19px; margin-bottom: 4px; }
  .person__title, .person__address { color: var(--muted); font-size: 13px; line-height: 1.4; }

  .divider {
    position: absolute; top: 150px; left: 262px; width: 1px; height: 110px;
    background: #9a9a9a;
  }

  .contacts { position: absolute; top: 168px; left: 286px; list-style: none; }
  .contacts__item {
    display: flex; align-items: center; gap: 10px;
    color: var(--ink); font-size: 14px; line-height: 22px;
  }
  .contacts__icon { width: 13px; height: 13px; flex: none; fill: var(--sky); }

  .band { position: absolute; bottom: 0; height: 12px; }
  .band--navy { left: 0; width: 50%; background: var(--navy); }
  .band--sky { right: 0; width: 50%; background: var(--sky); }
</style>
</head>
<body>
<main class="sheet">
  <section class="card card--back" aria-label="Card back">
    <div class="brand">
      <span class="brand__dot"></span>
      <span class="brand__name">Marwell Law</span>
    </div>
    <div class="rule"></div>
  </section>

  <section class="card card--front" aria-label="Card front">
    <div class="brand">
      <span class="brand__dot"></span>
      <span class="brand__name">Marwell Law</span>
    </div>
    <div class="rule"></div>

    <div class="person">
      <p class="person__name">Daniel Hughes</p>
      <p class="person__title">Managing Director</p>
      <p class="person__address">4120 Birchwood Lane<br>Juneau, Alaska 99801</p>
    </div>

    <div class="divider"></div>

    <ul class="contacts">
      <li class="contacts__item">
        <svg class="contacts__icon" viewBox="0 0 16 16"><path d="M3 1l3 1 1 3-2 1.5a9 9 0 0 0 4.5 4.5L11 9l3 1 1 3-2 2C7 15 1 9 1 3z"/></svg>
        555-210-4836
      </li>
      <li class="contacts__item">
        <svg class="contacts__icon" viewBox="0 0 16 16"><path d="M4 0h8a1 1 0 0 1 1 1v14a1 1 0 0 1-1 1H4a1 1 0 0 1-1-1V1a1 1 0 0 1 1-1zm1 2v10h6V2z"/></svg>
        555-319-7742
      </li>
      <li class="contacts__item">
        <svg class="contacts__icon" viewBox="0 0 16 16"><path d="M0 3h16v1L8 9 0 4zM0 6l8 5 8-5v7H0z"/></svg>
        info@marwelllaw.com
      </li>
      <li class="contacts__item">
        <svg class="contacts__icon" viewBox="0 0 16 16"><circle cx="8" cy="8" r="7.5"/><path d="M0.5 8h15M8 0.5c-3 3.5-3 11.5 0 15M8 0.5c3 3.5 3 11.5 0 15" stroke="#f7f8f9" stroke-width="1" fill="none"/></svg>
        www.marwelllaw.com
      </li>
    </ul>

    <div class="band band--navy"></div>
    <div class="band band--sky"></div>
  </section>
</main>
</body>
</html>
```